Maple Junction: PowerPoint Design Project

I'm looking for a PowerPoint design that my real estate ompany will use for business proposals and presentations.
Updates

Project Deadline Extended
Reason: I'm making the contest "guaranteed payment" as requested by some designers. I'll be using the PowerPoint slides for client presentations. The tag lines given can be a footer or watermark because it just give an idea of what we do and what our company values are.

Target Market(s)

Landlords and corporate companies

Industry/Entity Type

Real Estate

Requirements
Must have
• Company logo
Various Tag lines as a part of the design of the PowerPoint:
1st tagline: we don't just build your business, we build your community
2nd tag line: we excel in generating revenue, enhancing the guest experience and protecting the brand.
3rd tag line: we are all about people, projects and profits

```html
<!DOCTYPE html>
<html lang="en">
<head>
<meta charset="utf-8">
<title>Maple Junction Property Consultants – Title Slide</title>
<link rel="stylesheet" href="https://fonts.googleapis.com/css2?family=Carlito:wght@700&family=Oswald:wght@500;600&display=swap">
<style>
  :root {
    --bg-light: #f3fdea;
    --bg-mid: #dcf7c4;
    --bg-deep: #c6ee9f;
    --oval-black: #020202;
    --band-green: #6fae2e;
    --band-purple: #8d1ba4;
    --title-top: #a8e07a;
    --title-bottom: #3f8f1d;
    --subtitle: #b5df86;
    --brand-purple: #9a1fb2;
    --tagline-grey: #3a3a3a;
    --badge-white: #ffffff;
  }
  * { margin: 0; padding: 0; box-sizing: border-box; }
  html, body { width: 1200px; height: 900px; overflow: hidden; }
  body { background: var(--bg-light); }

  .slide {
    position: relative;
    width: 1200px;
    height: 900px;
    overflow: hidden;
    background: radial-gradient(ellipse at 85% 20%, var(--bg-deep) 0%, var(--bg-mid) 45%, var(--bg-light) 100%);
  }

  .swoosh { position: absolute; inset: 0; width: 1200px; height: 900px; }

  .title-block {
    position: absolute;
    left: 0;
    top: 200px;
    width: 1200px;
    text-align: center;
    font-family: "Carlito", "Calibri", sans-serif;
  }
  .title {
    font-size: 84px;
    font-weight: 700;
    line-height: 1;
    letter-spacing: 1px;
    background: linear-gradient(180deg, var(--title-top) 0%, var(--title-bottom) 100%);
    -webkit-background-clip: text;
    background-clip: text;
    color: transparent;
  }
  .title-reflection {
    font-size: 84px;
    font-weight: 700;
    line-height: 1;
    letter-spacing: 1px;
    height: 34px;
    overflow: hidden;
    transform: scaleY(-1);
    color: var(--title-bottom);
    opacity: 0.55;
    -webkit-mask-image: linear-gradient(0deg, rgba(0,0,0,0.9), rgba(0,0,0,0));
    mask-image: linear-gradient(0deg, rgba(0,0,0,0.9), rgba(0,0,0,0));
    display: flex;
    align-items: flex-end;
    justify-content: center;
    margin-top: -6px;
  }
  .subtitle {
    position: absolute;
    left: 0;
    top: 308px;
    width: 1200px;
    text-align: center;
    font-family: "Carlito", "Calibri", sans-serif;
    font-size: 36px;
    font-weight: 700;
    color: var(--subtitle);
  }

  .brand {
    position: absolute;
    left: 0;
    top: 720px;
    width: 1200px;
    text-align: center;
  }
  .brand-badge {
    width: 92px;
    height: 92px;
    border-radius: 50%;
    background: var(--badge-white);
    margin: 0 auto 22px;
  }
  .brand-name {
    font-family: "Oswald", "Impact", sans-serif;
    font-weight: 600;
    font-size: 24px;
    line-height: 1.1;
    color: var(--brand-purple);
  }
  .brand-tagline {
    font-family: "Oswald", "Impact", sans-serif;
    font-weight: 500;
    font-size: 14px;
    line-height: 1.6;
    color: var(--tagline-grey);
  }
</style>
</head>
<body>
  <main class="slide">
    <svg class="swoosh" viewBox="0 0 1200 900" aria-hidden="true">
      <defs>
        <radialGradient id="oval-sheen" cx="50%" cy="35%" r="60%">
          <stop offset="0%" stop-color="#0a0a0a"/>
          <stop offset="85%" stop-color="#000000"/>
          <stop offset="100%" stop-color="#1c1c1c"/>
        </radialGradient>
      </defs>
      <ellipse class="band-purple" cx="630" cy="340" rx="700" ry="335" transform="rotate(-6 630 340)" fill="var(--band-purple)"/>
      <ellipse class="band-green" cx="615" cy="318" rx="688" ry="318" transform="rotate(-5 615 318)" fill="var(--band-green)"/>
      <ellipse class="oval" cx="585" cy="292" rx="680" ry="308" transform="rotate(-2 585 292)" fill="url(#oval-sheen)"/>
    </svg>

    <header class="title-block">
      <h1 class="title">Title of Presentation</h1>
      <div class="title-reflection" aria-hidden="true">Title of Presentation</div>
    </header>
    <p class="subtitle">Sub Title of Presentation</p>

    <footer class="brand">
      <div class="brand-badge"></div>
      <p class="brand-name">Maple Junction Property Consultants</p>
      <p class="brand-tagline">Experiential Retail and Turn Around Professionals</p>
    </footer>
  </main>
</body>
</html>
```